Cool business cards

Use my existing logo from tallow brook (see images I have uploaded) and design a really cool non-stuffy business card. I am a divorce mediator.

```html
<!DOCTYPE html>
<html lang="en">
<head>
<meta charset="utf-8">
<title>Tallow Brook, J.D. — Business Cards</title>
<link href="https://fonts.googleapis.com/css2?family=Montserrat:wght@700;800&family=Questrial&family=Arimo&display=swap" rel="stylesheet">
<style>
  :root {
    --stage: #000000;
    --card-white: #ffffff;
    --card-edge: #9a9a9a;
    --brand-blue: #0a68ae;
    --brand-orange: #f28a21;
    --soft-grey: #8e8e8e;
    --white: #ffffff;
  }
  * { margin: 0; padding: 0; box-sizing: border-box; }
  html, body {
    width: 1200px; height: 1001px; overflow: hidden;
    background: var(--stage);
  }
  .stage { position: relative; width: 1200px; height: 1001px; }

  .card {
    position: absolute; left: 243px; width: 705px; height: 403px;
  }
  .card--front { top: 72px; background: var(--card-white); border: 1px solid var(--card-edge); }
  .card--back { top: 517px; background: var(--brand-blue); }

  .lockup { position: absolute; text-align: center; }
  .lockup__dot { border-radius: 50%; margin: 0 auto; }
  .lockup__name {
    font-family: "Montserrat", sans-serif; font-weight: 800;
    letter-spacing: 0.5px; white-space: nowrap;
  }
  .lockup__tag {
    display: flex; align-items: center; justify-content: center;
    font-family: "Montserrat", sans-serif; font-weight: 700;
    color: var(--soft-grey); white-space: nowrap; letter-spacing: 0.3px;
  }
  .lockup__tag::before, .lockup__tag::after {
    content: ""; display: block; height: 2px; background: var(--soft-grey);
  }

  .card--front .lockup { left: 0; right: 0; top: 99px; }
  .card--front .lockup__dot { width: 124px; height: 124px; background: var(--brand-orange); }
  .card--front .lockup__name { margin-top: 20px; font-size: 27px; color: var(--brand-blue); }
  .card--front .lockup__tag { margin-top: 2px; font-size: 12.5px; gap: 10px; }
  .card--front .lockup__tag::before, .card--front .lockup__tag::after { width: 22px; }

  .card--back .lockup { left: 20px; width: 300px; top: 123px; }
  .card--back .lockup__dot { width: 96px; height: 96px; background: var(--brand-orange); }
  .card--back .lockup__name { margin-top: 14px; font-size: 19px; color: var(--white); }
  .card--back .lockup__tag { margin-top: 1px; font-size: 10px; gap: 7px; }
  .card--back .lockup__tag::before, .card--back .lockup__tag::after { width: 18px; }

  .holder-name {
    position: absolute; left: 374px; top: 54px;
    font-family: "Questrial", sans-serif; font-size: 22px; color: var(--white);
  }
  .contact { position: absolute; left: 370px; top: 230px; list-style: none; }
  .contact__item {
    display: flex; align-items: center; height: 42px;
    font-family: "Arimo", sans-serif; font-size: 21.5px; color: var(--white);
  }
  .contact__icon { width: 26px; height: 26px; margin-right: 9px; flex: none; }
</style>
</head>
<body>
<main class="stage">
  <section class="card card--front" aria-label="Card front">
    <div class="lockup">
      <div class="lockup__dot"></div>
      <p class="lockup__name">TALLOW BROOK, J.D.</p>
      <p class="lockup__tag">DIVORCE &amp; FAMILY MEDIATION</p>
    </div>
  </section>

  <section class="card card--back" aria-label="Card back">
    <div class="lockup">
      <div class="lockup__dot"></div>
      <p class="lockup__name">TALLOW BROOK, J.D.</p>
      <p class="lockup__tag">DIVORCE &amp; FAMILY MEDIATION</p>
    </div>

    <p class="holder-name">NAME</p>

    <ul class="contact">
      <li class="contact__item">
        <svg class="contact__icon" viewBox="0 0 24 24" aria-hidden="true"><path fill="#fff" d="M6.6 2.5l3 3.4-1.8 2.4c1.4 2.9 3.5 5 6.4 6.4l2.4-1.8 3.4 3-1.6 3.4C11.2 19.6 4.4 12.8 3.2 4.1z"/></svg>
        +00 000000000
      </li>
      <li class="contact__item">
        <svg class="contact__icon" viewBox="0 0 24 24" aria-hidden="true"><rect x="1" y="5" width="22" height="14" fill="#fff"/><path d="M1.5 5.5l10.5 8 10.5-8M1.5 18.5l8-7M22.5 18.5l-8-7" fill="none" stroke="#0a68ae" stroke-width="1.6"/></svg>
        name@tallowbrook.com
      </li>
      <li class="contact__item">
        <svg class="contact__icon" viewBox="0 0 24 24" aria-hidden="true"><g fill="none" stroke="#fff" stroke-width="1.6"><circle cx="12" cy="12" r="10"/><ellipse cx="12" cy="12" rx="4.5" ry="10"/><path d="M2 12h20M4 6.5h16M4 17.5h16"/></g></svg>
        www.tallowbrook.com
      </li>
    </ul>
  </section>
</main>
</body>
</html>
```